Hadley & Partners, LLC Business Card 2016

We need a new business card design for a very important trade show coming up.

We are a compliance Consulting Firm. Our clients are stock brokerage firms and investment advisers.

I would like our logo on both sides of the card.

Info in the front of the card shold include:

Logo
First & Last Name
Title
Office #
Cell #
Email
Company Address (42 W. Calloway St., Suite 300 Pasadena, CA 91417

Back of the card should include the logo and url: www.hadleypartnersgroup.com

Target Market(s)

Stock Brokerage Firms and Investment Advisers

Industry/Entity Type

Financial Service

Contact Information for Business Card

Marcus J. Pellew
President
42 W. Calloway St., Suite 300
Pasadena, CA 91417
O 626.555.0147 ext. 204
C 818.555.0193
Email: marcus@hadleypartnersgroup.com
www.hadleypartnersgroup.com

Requirements
Nice to have
• The back of the card could be black with the logo with the white letters.
• I do want the front of the card to at least have the color logo with the black "Hadley & Partners Lettering.

```html
<!DOCTYPE html>
<html lang="en">
<head>
<meta charset="utf-8">
<title>Hadley &amp; Partners — Business Card</title>
<link href="https://fonts.googleapis.com/css2?family=Cinzel:wght@400;600&family=Nunito+Sans:wght@400&display=swap" rel="stylesheet">
<style>
  :root {
    --backdrop: #efefef;
    --card-white: #ffffff;
    --card-black: #000000;
    --brand-red: #cf2e27;
    --brand-slate: #5f6670;
    --ink: #111111;
    --rule: #6c6c6c;
    --paper-text: #ffffff;
  }
  * { margin: 0; padding: 0; box-sizing: border-box; }
  html, body { width: 1200px; height: 466px; overflow: hidden; }
  body { background: var(--backdrop); position: relative; }

  .card { position: absolute; top: 77px; width: 536px; height: 306px; overflow: hidden; }
  .card-front { left: 46px; background: var(--card-white); }
  .card-back { left: 622px; background: var(--card-black); }

  .bands { position: absolute; left: 0; top: 0; }

  .brand { position: absolute; text-align: center; font-family: "Cinzel", serif; font-weight: 600; }
  .brand-mark { display: block; margin: 0 auto; background: var(--brand-red); }
  .brand-name { display: block; line-height: 1; }
  .brand-sub { display: block; line-height: 1; letter-spacing: 0.28em; }

  .card-front .brand { left: 20px; top: 74px; width: 236px; color: var(--ink); }
  .card-front .brand-mark { width: 96px; height: 96px; margin-bottom: 30px; }
  .card-front .brand-name { font-size: 29px; letter-spacing: 0.02em; }
  .card-front .brand-sub { font-size: 13px; margin-top: 4px; }

  .divider { position: absolute; left: 236px; top: 42px; width: 1px; height: 232px; background: var(--rule); }

  .person { position: absolute; left: 256px; top: 44px; width: 250px; text-align: center; font-family: "Cinzel", serif; color: var(--ink); }
  .person-name { font-size: 26px; font-weight: 400; line-height: 1.1; }
  .person-title { font-size: 17px; font-weight: 400; margin-top: 4px; }

  .contact { position: absolute; left: 258px; top: 121px; list-style: none; font-family: "Nunito Sans", sans-serif; font-size: 14px; color: var(--ink); }
  .contact li { display: flex; align-items: flex-start; line-height: 21px; }
  .contact .icon { width: 16px; height: 21px; flex: none; margin-right: 4px; }
  .contact .gap { margin-top: 12px; }

  .card-back .brand { left: 0; top: 62px; width: 536px; color: var(--paper-text); }
  .card-back .brand-mark { width: 118px; height: 118px; margin-bottom: 28px; }
  .card-back .brand-name { font-size: 44px; letter-spacing: 0.02em; }
  .card-back .brand-sub { font-size: 20px; margin-top: 6px; }
</style>
</head>
<body>

<section class="card card-front" aria-label="Front of card">
  <svg class="bands" width="536" height="306" viewBox="0 0 536 306" aria-hidden="true">
    <polygon points="0,0 278,0 268,20 0,20" fill="var(--brand-slate)"/>
    <polygon points="284,0 536,0 536,20 274,20" fill="var(--brand-red)"/>
    <polygon points="0,284 262,284 250,306 0,306" fill="var(--brand-red)"/>
    <polygon points="264,293 536,293 536,306 256,306" fill="var(--brand-slate)"/>
  </svg>

  <div class="brand">
    <span class="brand-mark"></span>
    <span class="brand-name">HADLEY</span>
    <span class="brand-sub">&amp; PARTNERS</span>
  </div>

  <div class="divider"></div>

  <div class="person">
    <h1 class="person-name">Marcus Pellew</h1>
    <p class="person-title">President</p>
  </div>

  <ul class="contact">
    <li>
      <svg class="icon" viewBox="0 0 16 21" aria-hidden="true"><path d="M8 3.5a4.5 4.5 0 0 0-4.5 4.5c0 3.4 4.5 8 4.5 8s4.5-4.6 4.5-8A4.5 4.5 0 0 0 8 3.5z" fill="none" stroke="var(--ink)" stroke-width="1.4"/><circle cx="8" cy="8" r="1.6" fill="none" stroke="var(--ink)" stroke-width="1.3"/></svg>
      <span>42 W. Calloway St., Suite 300<br>Pasadena, CA 91417</span>
    </li>
    <li>
      <svg class="icon" viewBox="0 0 16 21" aria-hidden="true"><circle cx="8" cy="10.5" r="6.5" fill="none" stroke="var(--ink)" stroke-width="1.3"/><path d="M5.6 7.2l1.2-.4.9 1.7-.8.8a4 4 0 0 0 1.8 1.8l.8-.8 1.7.9-.4 1.2c-2.6.2-5.6-2.8-5.2-5.2z" fill="var(--ink)"/></svg>
      <span>O 626.555.0147 ext. 204<br>C 818.555.0193</span>
    </li>
    <li class="gap">
      <svg class="icon" viewBox="0 0 16 21" aria-hidden="true"><rect x="2" y="7" width="12" height="8" fill="var(--ink)"/><path d="M2 7l6 4.5L14 7" fill="none" stroke="var(--card-white)" stroke-width="1"/></svg>
      <span>marcus@hadleypartnersgroup.com</span>
    </li>
    <li>
      <svg class="icon" viewBox="0 0 16 21" aria-hidden="true"><circle cx="8" cy="10.5" r="5.5" fill="none" stroke="var(--ink)" stroke-width="1.1"/><ellipse cx="8" cy="10.5" rx="2.4" ry="5.5" fill="none" stroke="var(--ink)" stroke-width="1"/><path d="M2.5 10.5h11" stroke="var(--ink)" stroke-width="1"/></svg>
      <span>www.hadleypartnersgroup.com</span>
    </li>
  </ul>
</section>

<section class="card card-back" aria-label="Back of card">
  <div class="brand">
    <span class="brand-mark"></span>
    <span class="brand-name">HADLEY</span>
    <span class="brand-sub">&amp; PARTNERS</span>
  </div>
</section>

</body>
</html>
```